Business Card Design Project

Taprilo - based in Harwick Bay, Veralia. We plan, design, implement and support network infrastructure (Vorda, Halvest, K8, Tarnwick etc).

Target Market(s)

Small/Medium enterprise and Corporate.

Industry/Entity Type

Business

```html
<!DOCTYPE html>
<html lang="en">
<head>
<meta charset="utf-8">
<title>Taprilo business card</title>
<link href="https://fonts.googleapis.com/css2?family=Arimo:wght@400;700&display=swap" rel="stylesheet">
<style>
  :root {
    --page-bg: #e4e4e6;
    --card-white: #ffffff;
    --card-grey: #6a6a6c;
    --mark-grey: #9d9d9f;
    --text-grey: #6b6b6d;
    --brand-orange: #d97b0b;
    --rule-grey: #a8a8aa;
    --ink-white: #ffffff;
  }
  * { box-sizing: border-box; margin: 0; padding: 0; }
  html, body {
    width: 1200px; height: 900px; overflow: hidden;
    background: var(--page-bg);
    font-family: "Arimo", Arial, sans-serif;
  }
  .sheet {
    width: 1200px; height: 900px;
    display: flex; flex-direction: column; align-items: center; justify-content: center;
    gap: 44px;
  }
  .card {
    width: 640px; height: 356px; position: relative; overflow: hidden;
    box-shadow: 0 8px 24px rgba(0,0,0,0.12);
  }

  /* Back */
  .card-back { background: var(--card-grey); }
  .card-back .back-disc {
    position: absolute; right: -70px; top: -110px;
    width: 380px; height: 380px; border-radius: 50%;
    background: var(--mark-grey);
  }
  .card-back .back-name {
    position: absolute; left: 52px; bottom: 56px;
    color: var(--ink-white); font-size: 38px; font-weight: 400; letter-spacing: 0.5px;
  }

  /* Front */
  .card-front { background: var(--card-white); }
  .front-brand {
    position: absolute; left: 150px; top: 34px;
    display: flex; align-items: center; gap: 14px;
  }
  .brand-dot {
    width: 62px; height: 62px; border-radius: 50%; background: var(--text-grey);
  }
  .brand-name {
    font-size: 66px; font-weight: 400; color: var(--text-grey); letter-spacing: -1px; line-height: 1;
  }
  .name-band {
    position: absolute; left: 0; right: 0; top: 128px; height: 76px;
    background: var(--brand-orange);
    display: flex; align-items: center; padding-left: 168px;
    color: var(--ink-white);
  }
  .person-name { font-size: 34px; font-weight: 700; letter-spacing: 1px; }
  .band-rule { width: 2px; height: 32px; background: var(--ink-white); margin: 0 18px; opacity: .9; }
  .person-role { font-size: 30px; font-weight: 400; letter-spacing: 1px; }

  .contact-row {
    position: absolute; left: 0; right: 0; top: 224px; height: 104px;
    display: flex; align-items: flex-end;
    color: var(--text-grey); font-size: 19px; line-height: 1.25;
  }
  .contact-col { padding: 0 22px; white-space: nowrap; }
  .contact-address { padding-left: 52px; width: 248px; }
  .contact-rule { width: 1.5px; align-self: stretch; background: var(--rule-grey); }
  .contact-phones { align-self: flex-start; padding-top: 6px; }
  .contact-web { align-self: flex-start; padding-top: 6px; }
</style>
</head>
<body>
<main class="sheet">
  <section class="card card-back" aria-label="Card back">
    <div class="back-disc"></div>
    <p class="back-name">taprilo</p>
  </section>

  <section class="card card-front" aria-label="Card front">
    <div class="front-brand">
      <span class="brand-dot"></span>
      <span class="brand-name">taprilo</span>
    </div>
    <div class="name-band">
      <span class="person-name">Marek Olsen</span>
      <span class="band-rule"></span>
      <span class="person-role">CEO</span>
    </div>
    <div class="contact-row">
      <div class="contact-col contact-address">taprilo network<br>Harwick Bay, Veralia</div>
      <div class="contact-rule"></div>
      <div class="contact-col contact-phones">+61 3 5550 1842<br>+61 4 5550 7316</div>
      <div class="contact-rule"></div>
      <div class="contact-col contact-web">info@taprilo.net<br>www.taprilo.net</div>
    </div>
  </section>
</main>
</body>
</html>
```